Business card for Chiropractic clinics needs reworked / redesigned

The business card in attachment was designed 10 years ago. It is in need of an update.
We have 2 clinics:
VELDHOVE KLINIEK & VELDHOVE KLINIEK NOORD
Only one address needs to be on the card for doctors that only work in one clinic and two addresses need to be on the card for the doctors that work in both clinics.

Target Market(s)

patients/referrers

Industry/Entity Type

Medical

Contact Information for Business Card

Logo (in full or zoomed-in)
Clinic Name
Doctor name and title
clinic address, website, tel, email

Font styles to use
Sans Serif

Colors

Designer to choose colors to be used in the design.

Requirements
Must have
• Good contrast/readability
• We like modern minimalistic designs
• The Bcard needs to project our very high standard of proficiency/professionalism
Should not have
• Not curly
• Not to much colours

```html
<!DOCTYPE html>
<html lang="nl">
<head>
<meta charset="utf-8">
<title>Veldhove Kliniek – visitekaartje</title>
<link href="https://fonts.googleapis.com/css2?family=Open+Sans:wght@400;600;700&display=swap" rel="stylesheet">
<style>
  :root {
    --backdrop: #939498;
    --clinic-green: #124a3c;
    --mark-green: #2a5f51;
    --card-white: #ffffff;
    --title-grey: #6d6e70;
    --faint-grey: #d9dcd9;
  }
  * { margin: 0; padding: 0; box-sizing: border-box; }
  html, body {
    width: 1200px; height: 1000px; overflow: hidden;
    background: var(--backdrop);
    font-family: "Open Sans", Arial, sans-serif;
  }
  .canvas { position: relative; width: 1200px; height: 1000px; }
  .card {
    position: absolute; top: 324px; width: 558px; height: 372px; overflow: hidden;
  }
  .card--front { left: 22px; background: var(--card-white); }
  .card--back { left: 618px; background: var(--clinic-green); }

  .front-decoration {
    position: absolute; left: 14px; top: 0; width: 170px; height: 372px;
    background: linear-gradient(90deg, rgba(217,220,217,0) 0%, rgba(217,220,217,0.55) 50%, rgba(217,220,217,0) 100%);
  }

  .doctor {
    position: absolute; right: 24px; top: 60px; text-align: right;
  }
  .doctor__name {
    color: var(--clinic-green); font-weight: 700; font-size: 21px;
    line-height: 26px; letter-spacing: 0.2px;
  }
  .doctor__title {
    color: var(--title-grey); font-size: 17px; line-height: 19px;
  }
  .doctor__number {
    color: var(--title-grey); font-size: 12px; line-height: 16px;
    letter-spacing: 3.4px; margin-right: -3px;
  }

  .contact-band {
    position: absolute; left: 0; top: 249px; width: 100%; height: 97px;
    background: var(--clinic-green);
  }
  .front-decoration--on-band {
    top: 249px; height: 97px;
    background: linear-gradient(90deg, rgba(255,255,255,0) 0%, rgba(255,255,255,0.12) 50%, rgba(255,255,255,0) 100%);
  }
  .clinic-name {
    position: absolute; left: 224px; top: 221px;
    color: var(--clinic-green); font-weight: 700; font-size: 27px; line-height: 32px;
    letter-spacing: -0.3px;
  }
  .contact-list {
    position: absolute; left: 225px; top: 252px; list-style: none;
    color: var(--card-white); font-size: 14px; line-height: 19px;
  }

  .back-mark {
    position: absolute; left: 189px; top: 66px; width: 180px; height: 180px;
    border-radius: 50%; background: var(--mark-green);
  }
  .back-rule {
    position: absolute; left: 0; top: 320px; width: 100%; height: 2px;
    background: var(--card-white);
  }
  .back-name {
    position: absolute; left: 0; top: 278px; width: 100%; text-align: center;
    color: var(--card-white); font-size: 27px; line-height: 34px; letter-spacing: 0.3px;
  }
</style>
</head>
<body>
<main class="canvas">
  <section class="card card--front" aria-label="Voorzijde visitekaartje">
    <div class="front-decoration" role="img" aria-label="Zachte decoratieve zone voor het kliniekembleem"></div>
    <div class="doctor">
      <p class="doctor__name">PIETER VANDAMME D.C.</p>
      <p class="doctor__title">CHIROPRACTOR</p>
      <p class="doctor__number">07246315800</p>
    </div>
    <div class="contact-band"></div>
    <div class="front-decoration front-decoration--on-band" aria-hidden="true"></div>
    <h1 class="clinic-name">VELDHOVE KLINIEK</h1>
    <ul class="contact-list">
      <li>Kouterlaan 118</li>
      <li>9050 veldhove</li>
      <li>09 345 18 20</li>
      <li>info@veldhovekliniek.be</li>
      <li>www.veldhovekliniek.be</li>
    </ul>
  </section>

  <section class="card card--back" aria-label="Achterzijde visitekaartje">
    <div class="back-mark" aria-hidden="true"></div>
    <p class="back-name">VELDHOVE KLINIEK</p>
    <div class="back-rule"></div>
  </section>
</main>
</body>
</html>
```